Talvern Asset Management - Corporate Letter Head Project

Looking for a classy design based on our current logo. Please find current logo source file in files. With our color scheme.

Target Market(s)

We're an investment firm, the letterhead needs to look professional and attractive to clients.

Industry/Entity Type

Hedgefund

Colors
0054AA
0677BA
7BADD7
CADEEF
E8F1F8

Requirements
Must have
• Our logo, address, phone number, and email

```html
<!DOCTYPE html>
<html lang="en">
<head>
<meta charset="utf-8">
<title>Talvern Asset Management – Letterhead</title>
<link rel="stylesheet" href="https://fonts.googleapis.com/css2?family=Arimo&family=Montserrat:wght@400&family=Mulish:wght@800&display=swap">
<style>
  :root {
    --backdrop: #9b9a9b;
    --paper: #ffffff;
    --navy: #1b3058;
    --ink: #555555;
    --contact-ink: #5a5a5a;
    --signature-tone: #d9d9d9;
  }
  * { margin: 0; padding: 0; box-sizing: border-box; }
  html, body {
    width: 906px; height: 1200px; overflow: hidden;
    background: var(--backdrop);
  }
  .sheet {
    position: absolute; left: 104px; top: 107px;
    width: 698px; height: 987px;
    background: var(--paper);
    box-shadow: 3px 3px 5px rgba(0,0,0,0.35);
  }
  .company-name {
    position: absolute; left: 51px; top: 90px;
    font-family: "Montserrat", sans-serif; font-weight: 400;
    font-size: 15px; line-height: 18px; color: var(--navy);
    white-space: nowrap;
  }
  .rule-thick, .rule-thin {
    position: absolute; left: 0; right: 0; background: var(--navy);
  }
  .rule-thick { top: 116px; height: 7px; }
  .rule-thin { top: 127px; height: 2px; }
  .contact {
    position: absolute; left: 524px; top: 29px;
    font-family: "Montserrat", sans-serif; font-style: normal;
    font-size: 11.6px; color: var(--contact-ink); line-height: 13.7px;
  }
  .contact-address { margin-bottom: 5.5px; }
  .contact-line { display: flex; align-items: center; }
  .contact-line svg { width: 9px; height: 9px; margin-right: 5px; fill: var(--navy); }
  .letter {
    position: absolute; left: 63px; top: 303px;
    color: var(--ink);
  }
  .salutation {
    font-family: "Mulish", sans-serif; font-weight: 800;
    font-size: 16px; line-height: 20px; margin-bottom: 27px;
  }
  .body p {
    font-family: "Arimo", sans-serif; font-size: 12.3px;
    line-height: 14.4px; margin-bottom: 12.4px; white-space: nowrap;
  }
  .closing {
    font-family: "Mulish", sans-serif; font-weight: 800;
    font-size: 9px; margin-top: 22px;
  }
  .signature {
    width: 86px; height: 24px; margin-top: 30px;
    background: linear-gradient(90deg, var(--signature-tone), #ececec);
    border-radius: 3px;
  }
</style>
</head>
<body>
  <main class="sheet">
    <header>
      <div class="company-name">Talvern Asset Management</div>
      <div class="rule-thick"></div>
      <div class="rule-thin"></div>

      <address class="contact">
        <div class="contact-address">Your address, city<br>state, ZIP 0000</div>
        <div class="contact-line">
          <svg viewBox="0 0 10 10"><path d="M2 0.5 L3.8 2.5 L2.8 3.6 Q4 6 6.4 7.2 L7.5 6.2 L9.5 8 L8.3 9.5 Q2.5 8.5 0.5 1.7 Z"/></svg>
          <span>123-456-2100</span>
        </div>
        <div class="contact-line">
          <svg viewBox="0 0 10 10"><path d="M0.5 2 H9.5 V8 H0.5 Z M1 2.5 L5 5.5 L9 2.5" fill="var(--navy)" stroke="#fff" stroke-width="0.7"/></svg>
          <span>youremail@mailbox.com</span>
        </div>
        <div class="contact-line">
          <svg viewBox="0 0 10 10"><circle cx="5" cy="5" r="4.5"/><path d="M0.5 5 H9.5 M5 0.5 Q2.5 5 5 9.5 M5 0.5 Q7.5 5 5 9.5" fill="none" stroke="#fff" stroke-width="0.6"/></svg>
          <span>www.yourwebsite.com</span>
        </div>
      </address>
    </header>

    <section class="letter">
      <h1 class="salutation">Dear Mr. Halden,</h1>
      <div class="body">
        <p>Lorem ipsum dolor sit amet, consectetuer adipiscing elit, sed diam nonmmy nibh euismod tincidunt ut laor<br>eet dolore magna aliquam erat volutpat. Ut wisi enim ad minim veniam, quis nostrud exerci tationmcorper<br>suscipit lobortis nisl ut aliquip ex ea commodo consequat. Duis autem vel eum iriure dolor in hendrerit in<br>vulputate velit esse molestie consequat, vel illum dolore eu feugiat</p>
        <p>Rorem ipsum dolor sit amet, consectetuer adipiscing elit, sed diam nonmmy nibh euismod tincidunt ut laor<br>eet dolore magna aliquam erat volutpat. Ut wisi enim ad minim veniam, quis nostrud exerci tationmcorper<br>suscipit lobortis nisl ut aliquip ex ea commodo consequat. Duis autem vel eum iriure dolor in hendrerit in<br>vulputate velit esse molest</p>
        <p>Dorem ipsum dolor sit amet, consectetuer adipiscing elit, sed diam nonmmy nibh euismod tincidunt ut laor<br>eet dolore magna aliquam erat volutpat. Ut wisi enim ad minim veniam, quis nostrud exerci tationmcorper<br>suscipit lobortis nisl ut aliquip ex ea commodo consequat. Duis autem vel eum iriure dolor in hendrerit in<br>suscipit lobortis nisl ut aliquip ex ea commodo consequat. Duis autem vel eum iriure dolor in hendrerit in<br>vulputate velit esse molestie consequat, vel illum</p>
        <p>Sorem ipsum dolor sit amet, consectetuer adipiscing elit, sed diam nonmmy nibh euismod tincidunt ut laor<br>eet dolore magna aliquam erat volutpat. Ut wisi enim ad minim veniam, quis nostrud exerci tationmcorper<br>suscipit lobortis nisl ut aliquip ex ea commodo consequat. Duis autem vel eum iriure dolor in</p>
      </div>
      <p class="closing">Sincerely,</p>
      <div class="signature" role="img" aria-label="Handwritten signature of the sender"></div>
    </section>
  </main>
</body>
</html>
```